Website Design Requirements

Domain Name: NearbyBuildersIndex.example

Website Look: Simple, Clean, Modern, and Professional Awarding Winning Website. Our Platform is the Best Directory Platform, all we need is a very creative person to make the following designs and select the fonts, font sizing, font colors and all the colors for the color points. We will follow up with the winner of the contest to design the rest of our design needs. The highlight of our brand is our Mascot; we feel this is something everyone will remember. It may be the easiest to obtain a free trial of the platform from Marigold Listings to complete this project. When we pick a winner of this contest we will provide the password to our admin panel for everything to be applied. Our Competitors are Petras Board, House Scout and Pinwheel.

We are thinking a light gray scale shadowing or graduated ghosting for the background behind the image of the Mascot for the main image. We want the Mascot and the Selection box to stand out as well as the logo.

Design Elements:
Main Page Image-Size for website is 1800 X 600px should be the Mascot on the right half of the image; this is where creative design is the most important. Design can use the head only from the waist up or the full image

Logo- Size for website is 450 X 70px; the logo should have the head of the mascot on a 3D icon with 2 line of text to the right side. The top line should have Nearby Builders the second line should have the word Directory in smaller size and be ghosted. The main idea about the logo is the icon and the words Nearby Builder. Note example can be seen on the Marigold Listings Fast Launch Setup Primer on You Tube.

Favicon- Size for website is 56 X 56px should be the head of the mascot the Favicon and Google Map Pin drop could be the same if design is nice enough

Google Map Pin Drop- 25 X 46px should be the head of the mascot with a arrow pointing down.

Member Badge Image- Size 250 X 250px should be the head of the mascot inside a round ring with the words Verified –Certified –Member.

Target Market(s)

Consumers will use this website to locate Contractors in their Local area. Contractors will list their business on this website for a fee.

Industry/Entity Type

Domain

Contact Information for Business Card

Milo Berrant
Partner
555.014.2287
Milo@NearbyBuildersIndex.example
WWW. NearbyBuildersIndex.example

Logo Text

Nearby Builders Index

Number of Pages Required

3 page

Font styles to use
Serif

Colors
ec1f27
fbed22

Requirements
Must have
• The use of our mascot, you can use full body view, waist up or head shot
Nice to have
• Clean bright colored Mascot, listing on back of card
• Nearby Builders
• Electricians
• Plumbers
• HVAC
• Landscapers
• General Contractors
• Garage Door Repair
• Carpet Cleaners
• Concrete Contractors

```html
<!DOCTYPE html>
<html lang="en">
<head>
<meta charset="utf-8">
<title>Nearby Builders Index</title>
<link href="https://fonts.googleapis.com/css2?family=Open+Sans:wght@400;600;700;800&family=Montserrat:wght@600;700&display=swap" rel="stylesheet">
<style>
:root{
  --red:#e8232a;
  --red-soft:rgba(214,60,66,.72);
  --orange:#e28e00;
  --white:#ffffff;
  --ink:#111111;
  --grey-dark:#3d3d3d;
  --black:#0b0b0b;
  --hero-light:#f2f2f2;
  --hero-mid:#b9b9b9;
  --line:#9a9a9a;
}
*{box-sizing:border-box;margin:0;padding:0}
html,body{width:1200px;height:3600px;overflow:hidden;background:var(--white)}
body{position:relative;font-family:"Open Sans",Arial,sans-serif;color:var(--ink)}
.abs{position:absolute}

/* header */
.site-header{left:0;top:0;width:1200px;height:108px;background:var(--white)}
.brand{left:115px;top:18px;display:flex;align-items:center;gap:12px}
.brand-mark{width:70px;height:70px;border-radius:50%;background:var(--red)}
.brand-name{font-weight:800;color:var(--red);font-size:27px;line-height:28px;letter-spacing:.5px}
.member-login{left:728px;top:4px;font-size:19px;font-weight:600}
.member-tab{left:868px;top:0;width:162px;height:36px;background:var(--red)}
.field{height:40px;border:1.5px solid #bbb;background:var(--white);display:flex;align-items:center;gap:10px;padding-left:14px;font-style:italic;font-size:20px;color:#555}
.field-tools{left:523px;top:60px;width:217px}
.field-filter{left:753px;top:60px;width:214px}
.search-btn{left:980px;top:60px;width:48px;height:40px;background:var(--red);display:flex;align-items:center;justify-content:center}

/* nav */
.main-nav{left:0;top:108px;width:1200px;height:74px;background:var(--red);display:flex}
.main-nav a{color:var(--white);text-decoration:none;font-size:28px;display:flex;align-items:center;justify-content:center;border-right:2px solid rgba(255,255,255,.55)}
.main-nav a:last-child{border-right:none}

/* hero */
.hero{left:0;top:182px;width:1200px;height:473px;background:linear-gradient(90deg,var(--hero-light) 0%,#d6d6d6 40%,var(--hero-mid) 70%,#8f8f8f 100%)}
.hero-title{left:118px;top:16px;font-size:54px;font-weight:700;line-height:72px;color:var(--ink)}
.finder{left:118px;top:183px;width:562px;height:177px;background:var(--red-soft);border-radius:8px;padding:16px 0 0 0}
.finder-row{position:absolute;display:flex;align-items:center}
.finder-label{width:240px;text-align:right;color:var(--white);font-weight:600;font-size:25px;padding-right:14px}
.finder-input{width:282px;height:42px;background:var(--white);display:flex;align-items:center;gap:8px;padding-left:12px;font-family:Georgia,serif;font-size:18px;color:#777}
.finder-go{left:258px;top:120px;width:282px;height:40px;background:var(--red);color:var(--white);font-size:24px;display:flex;align-items:center;justify-content:center}
.mascot{left:710px;top:0;width:320px;height:473px;background:radial-gradient(ellipse at 50% 55%,#f0c530 0%,#e2423b 55%,rgba(180,180,180,0) 80%)}

/* service cards */
.card-img{width:178px;height:133px}
.card-text{width:230px;font-size:17px;line-height:22px}
.card-text b{display:block;font-weight:700;margin-bottom:8px}
.more{display:block;text-align:right;font-size:15px;text-decoration:underline;margin-top:6px}

/* news strips */
.strip{left:0;width:1200px}
.strip-latest{top:1092px;height:243px;background:var(--orange)}
.strip-featured{top:2120px;height:268px;background:var(--red)}
.strip-title{width:1200px;text-align:center;color:var(--white);font-weight:700}
.thumb{width:138px;height:135px}
.thumb-label{width:160px;text-align:center;color:var(--white);font-weight:700;font-size:17px}

/* house banner */
.house{left:0;top:1335px;width:1200px;height:580px;background:linear-gradient(180deg,#3f7fd6 0%,#9cc3ee 38%,#9b8a72 60%,#6f5a45 82%,#4e7c32 100%)}
.house-title{left:180px;top:12px;font-family:Montserrat,Arial,sans-serif;font-weight:700;font-size:58px;color:var(--white)}
.house-sub{left:180px;top:80px;width:440px;font-size:26px;line-height:30px;color:var(--ink)}

/* newsletter */
.newsletter{left:0;top:1915px;width:1200px;height:205px;background:var(--orange)}
.newsletter-title{width:1200px;text-align:center;top:14px;font-family:Montserrat,Arial,sans-serif;font-weight:700;font-size:46px;color:var(--white)}
.nl-box{background:var(--white);height:60px;display:flex;align-items:center;padding-left:24px;font-size:32px}

/* articles */
.article-img{width:245px;height:175px}
.article-title{width:360px;text-align:center;font-weight:700;font-size:25px;line-height:34px}
.article-body{width:360px;text-align:center;font-size:20px;line-height:28px}
.article-more{width:360px;text-align:center;font-size:16px;text-decoration:underline}

/* footer */
.site-footer{left:0;top:3220px;width:1200px;height:275px;background:var(--grey-dark);color:var(--white)}
.foot-brand{left:158px;top:32px;display:flex;align-items:center;gap:8px}
.foot-brand .brand-mark{width:40px;height:40px}
.foot-brand .brand-name{color:var(--white);font-size:15px;line-height:16px}
.foot-about{left:152px;top:108px;width:180px;font-size:17px;line-height:21px;text-align:justify}
.foot-more{left:208px;top:212px;font-weight:700;font-size:16px}
.foot-head{font-weight:700;font-size:21px}
.foot-list{font-size:21px;line-height:26px}
.social{left:906px;top:85px;display:flex;gap:17px}
.social span{width:40px;height:40px;border-radius:50%;background:var(--white)}
.copyright{left:0;top:3495px;width:1200px;height:105px;background:var(--black);color:var(--white);text-align:center;font-size:21px;padding-top:28px}
</style>
</head>
<body>

<header class="abs site-header">
  <div class="abs brand">
    <span class="brand-mark"></span>
    <span class="brand-name">NEARBY BUILDERS<br>INDEX</span>
  </div>
  <div class="abs member-login">Member login</div>
  <div class="abs member-tab"></div>
  <div class="abs field field-tools">
    <svg width="22" height="22" viewBox="0 0 24 24"><path d="M14 3a5 5 0 0 0-4.6 6.9L3 16.3 5.7 19l6.4-6.4A5 5 0 0 0 19 8l-3 1-2-2 1-3z" fill="#666"/></svg>Tools
  </div>
  <div class="abs field field-filter">
    <svg width="20" height="20" viewBox="0 0 24 24"><path d="M2 3h20l-8 9v8l-4 2V12z" fill="#666"/></svg>Filter
  </div>
  <div class="abs search-btn">
    <svg width="26" height="26" viewBox="0 0 24 24"><circle cx="10" cy="10" r="6.5" fill="none" stroke="#fff" stroke-width="3"/><path d="M15 15l6 6" stroke="#fff" stroke-width="3.5" stroke-linecap="round"/></svg>
  </div>
</header>

<nav class="abs main-nav">
  <a href="#" style="width:298px">HOME</a>
  <a href="#" style="width:284px">OUR WORK</a>
  <a href="#" style="width:236px">BLOG</a>
  <a href="#" style="width:382px;justify-content:flex-start;padding-left:36px">CONTACT US</a>
</nav>

<section class="abs hero">
  <h1 class="abs hero-title">It is a long established<br>fact that a reader</h1>
  <div class="abs finder">
    <div class="finder-row" style="top:12px;left:0">
      <span class="finder-label">What do you need?</span>
      <span class="finder-input"><svg width="18" height="18" viewBox="0 0 24 24"><circle cx="10" cy="10" r="6.5" fill="none" stroke="#777" stroke-width="2.5"/><path d="M15 15l6 6" stroke="#777" stroke-width="3"/></svg>Enter Keyword</span>
    </div>
    <div class="finder-row" style="top:64px;left:0">
      <span class="finder-label">Located in:</span>
      <span class="finder-input"><svg width="16" height="20" viewBox="0 0 16 22"><path d="M8 0a8 8 0 0 0-8 8c0 6 8 14 8 14s8-8 8-14a8 8 0 0 0-8-8z" fill="#666"/><circle cx="8" cy="8" r="3" fill="#fff"/></svg>Enter City or Post code</span>
    </div>
    <div class="abs finder-go">Search Now</div>
  </div>
  <div class="abs mascot" role="img" aria-label="Smiling builder mascot in yellow hard hat and red shirt, arms crossed"></div>
</section>

<section class="abs" style="left:0;top:655px;width:1200px;height:437px">
  <div class="abs card-img" style="left:150px;top:50px;background:linear-gradient(180deg,#a9c4dc,#e6e6e6 55%,#7d8a5a)" role="img" aria-label="White two-storey house"></div>
  <div class="abs card-text" style="left:343px;top:50px"><b>when an unknown printer took a galley of type</b>when an unknown printer took a galley of type.<span class="more">MORE</span></div>
  <div class="abs card-img" style="left:635px;top:50px;background:linear-gradient(180deg,#5d7a3a,#8a7a4a)" role="img" aria-label="Workers on a landscaping site"></div>
  <div class="abs card-text" style="left:838px;top:50px"><b>when an unknown printer took a galley of type</b>when an unknown printer took a galley of type.<span class="more">MORE</span></div>
  <div class="abs card-img" style="left:150px;top:220px;background:linear-gradient(180deg,#d8b24a,#8a6a3a)" role="img" aria-label="Workers inside a building under construction"></div>
  <div class="abs card-text" style="left:343px;top:220px"><b>when an unknown printer took a galley of type</b>when an unknown printer took a galley of type.<span class="more">MORE</span></div>
  <div class="abs card-img" style="left:635px;top:220px;background:linear-gradient(180deg,#cfd6dc,#3a3a3a)" role="img" aria-label="Excavator arm at a work site"></div>
  <div class="abs card-text" style="left:838px;top:220px"><b>when an unknown printer took a galley of type</b>when an unknown printer took a galley of type.<span class="more">MORE</span></div>
</section>

<section class="abs strip strip-latest">
  <div class="abs strip-title" style="top:18px;font-size:31px">Latest News</div>
  <svg class="abs" style="left:106px;top:110px" width="32" height="36" viewBox="0 0 32 36"><path d="M30 0L0 18l30 18-10-18z" fill="#fff"/></svg>
  <svg class="abs" style="left:1040px;top:110px" width="32" height="36" viewBox="0 0 32 36"><path d="M2 0l30 18L2 36l10-18z" fill="#fff"/></svg>
  <div class="abs thumb" style="left:168px;top:71px;background:linear-gradient(160deg,#e6d26a,#5a6a7a)" role="img" aria-label="Engineers reviewing plans"></div>
  <div class="abs thumb" style="left:348px;top:71px;background:linear-gradient(160deg,#f1f1f1,#8a3a2a)" role="img" aria-label="Worker on phone in hard hat"></div>
  <div class="abs thumb" style="left:525px;top:71px;background:linear-gradient(160deg,#c9a45a,#6a5030)" role="img" aria-label="Builders on timber frame"></div>
  <div class="abs thumb" style="left:700px;top:71px;background:linear-gradient(160deg,#dfe3e6,#4a5a6a)" role="img" aria-label="Engineers with laptop on site"></div>
  <div class="abs thumb" style="left:878px;top:71px;background:linear-gradient(160deg,#e8c23a,#2a3a5a)" role="img" aria-label="Worker in safety vest"></div>
  <div class="abs thumb-label" style="left:157px;top:212px">LOREM IPSUM</div>
  <div class="abs thumb-label" style="left:337px;top:212px">LOREM IPSUM</div>
  <div class="abs thumb-label" style="left:514px;top:212px">LOREM IPSUM</div>
  <div class="abs thumb-label" style="left:689px;top:212px">LOREM IPSUM</div>
  <div class="abs thumb-label" style="left:867px;top:212px">LOREM IPSUM</div>
</section>

<section class="abs house" role="img" aria-label="Large two-storey stone and siding family house under blue sky">
  <h2 class="abs house-title">Lorem ipsum</h2>
  <p class="abs house-sub">Lorem Ipsum is simply dummy text of the printing and typesetting</p>
</section>

<section class="abs newsletter">
  <h2 class="abs newsletter-title">News Letter</h2>
  <div class="abs nl-box" style="left:163px;top:100px;width:482px">Email</div>
  <div class="abs nl-box" style="left:700px;top:100px;width:270px">Subcribe</div>
</section>

<section class="abs strip strip-featured">
  <div class="abs strip-title" style="top:12px;font-family:Montserrat,Arial,sans-serif;font-size:46px">Featured News</div>
  <svg class="abs" style="left:106px;top:130px" width="32" height="36" viewBox="0 0 32 36"><path d="M30 0L0 18l30 18-10-18z" fill="#fff"/></svg>
  <svg class="abs" style="left:1040px;top:130px" width="32" height="36" viewBox="0 0 32 36"><path d="M2 0l30 18L2 36l10-18z" fill="#fff"/></svg>
  <div class="abs thumb" style="left:152px;top:88px;width:155px;background:linear-gradient(160deg,#b9c6d2,#7a5a3a)" role="img" aria-label="Site meeting at new build"></div>
  <div class="abs thumb" style="left:333px;top:88px;width:150px;background:linear-gradient(160deg,#cdd8e2,#8a4a30)" role="img" aria-label="Brick house under construction"></div>
  <div class="abs thumb" style="left:518px;top:88px;width:133px;background:linear-gradient(160deg,#e2cfa0,#7a6040)" role="img" aria-label="Carpenters on roof frame"></div>
  <div class="abs thumb" style="left:688px;top:88px;width:150px;background:linear-gradient(160deg,#f0f0f0,#6a7a8a)" role="img" aria-label="Engineers reading blueprints"></div>
  <div class="abs thumb" style="left:866px;top:88px;width:157px;background:linear-gradient(160deg,#d9c08a,#5a5040)" role="img" aria-label="Builders at house frame"></div>
  <div class="abs thumb-label" style="left:157px;top:227px">LOREM IPSUM</div>
  <div class="abs thumb-label" style="left:328px;top:227px">LOREM IPSUM</div>
  <div class="abs thumb-label" style="left:505px;top:227px">LOREM IPSUM</div>
  <div class="abs thumb-label" style="left:683px;top:227px">LOREM IPSUM</div>
  <div class="abs thumb-label" style="left:864px;top:227px">LOREM IPSUM</div>
</section>

<section class="abs" style="left:0;top:2388px;width:1200px;height:832px">
  <div class="abs article-img" style="left:195px;top:32px;background:linear-gradient(160deg,#c2cfdb,#6a5a4a)" role="img" aria-label="Engineers below steel structure"></div>
  <div class="abs article-title" style="left:152px;top:222px">when an unknown printer took a galley of type</div>
  <div class="abs article-body" style="left:152px;top:298px">when an unknown printer took a galley of type.when an unknown printer took a galley of type.</div>
  <div class="abs article-more" style="left:140px;top:386px">MORE</div>

  <div class="abs article-img" style="left:708px;top:32px;background:linear-gradient(160deg,#e6e2da,#5a5a5a)" role="img" aria-label="Two engineers holding plans"></div>
  <div class="abs article-title" style="left:655px;top:222px">when an unknown printer took a galley of type</div>
  <div class="abs article-body" style="left:655px;top:298px">when an unknown printer took a galley of type.when an unknown printer took a galley of type.</div>
  <div class="abs article-more" style="left:643px;top:386px">MORE</div>

  <div class="abs article-img" style="left:195px;top:427px;background:linear-gradient(160deg,#dfe9ee,#8aa0ac)" role="img" aria-label="Engineers in glass atrium"></div>
  <div class="abs article-title" style="left:152px;top:620px">when an unknown printer took a galley of type</div>
  <div class="abs article-body" style="left:152px;top:696px">when an unknown printer took a galley of type.when an unknown printer took a galley of type.</div>
  <div class="abs article-more" style="left:140px;top:784px">MORE</div>

  <div class="abs article-img" style="left:708px;top:427px;background:linear-gradient(160deg,#e8d8b8,#7a5a40)" role="img" aria-label="Engineers reviewing plans indoors"></div>
  <div class="abs article-title" style="left:655px;top:620px">when an unknown printer took a galley of type</div>
  <div class="abs article-body" style="left:655px;top:696px">when an unknown printer took a galley of type.when an unknown printer took a galley of type.</div>
  <div class="abs article-more" style="left:643px;top:784px">MORE</div>
</section>

<footer class="abs site-footer">
  <div class="abs foot-brand"><span class="brand-mark"></span><span class="brand-name">NEARBY BUILDERS<br>INDEX</span></div>
  <p class="abs foot-about">Lorem Ipsum has been the industry's standard dummy text printer took a</p>
  <div class="abs foot-more">LOREM IPSUM</div>
  <div class="abs foot-head" style="left:374px;top:40px">Other Link</div>
  <div class="abs foot-list" style="left:371px;top:87px">Disclaimer &amp;Use Terms<br>Privacy policy<br>Site Map</div>
  <div class="abs foot-head" style="left:650px;top:35px">Location</div>
  <div class="abs foot-list" style="left:643px;top:85px">3481 Juniper Row<br>Alder Heights, CA 90000</div>
  <div class="abs foot-list" style="left:643px;top:156px">3481 Juniper Row<br>Alder Heights, CA 90000</div>
  <div class="abs foot-head" style="left:915px;top:35px">Around the Web</div>
  <div class="abs social"><span></span><span></span><span></span><span></span></div>
</footer>

<div class="abs copyright">All Right Reserved. Copy Right 2016 NearbyBuildersIndex.example</div>

</body>
</html>
```